A4 Flyer to introduce new line of ice cream cakes and dessert in a bakery shop

[The flyer should have written:]

Welcome to our new line of ice-cream desserts.

As everything else, all hand-made in our kitchen only with natural ingredients.

Try our new....

[then three sections with the following products]

* Ice-cream cakes
* Ice-creams
* Cookie ice-creams

Target Market(s)

Families

Industry/Entity Type

Shop

Font styles to use
Other font styles liked:
• Futura

Requirements
Must have
• Please include our logo on the flyer (see file attached)

```html
<!DOCTYPE html>
<html lang="en">
<head>
<meta charset="utf-8">
<title>Brinella – New Ice-Cream Desserts</title>
<link rel="stylesheet" href="https://fonts.googleapis.com/css2?family=Jost:wght@400;500;700&display=swap">
<style>
  :root {
    --gold: #b18a2c;
    --lavender: #efe9f3;
    --white: #ffffff;
    --berry: #d0479a;
    --lemon: #f4d33c;
    --lemon-light: #fff6b8;
    --lilac: #c89bd3;
    --lilac-light: #f3e4f6;
    --mint: #9fd37f;
    --mint-light: #e7f6d9;
  }
  * { box-sizing: border-box; margin: 0; padding: 0; }
  html, body { width: 798px; height: 1200px; overflow: hidden; }
  body { font-family: "Jost", "Futura", sans-serif; background: var(--lavender); }

  .flyer { position: relative; width: 798px; height: 1200px; overflow: hidden; background: var(--lavender); }
  .backdrop { position: absolute; inset: 0; }

  .logo-art {
    position: absolute; left: 180px; top: 34px; width: 300px; height: 150px;
    border-radius: 75px;
    background: radial-gradient(ellipse at center, #e3cf98 0%, #f6eedb 68%, rgba(255,255,255,0) 100%);
  }
  .brand-name {
    position: absolute; left: 52px; top: 178px;
    font-size: 112px; font-weight: 400; letter-spacing: 2px; line-height: 1;
    color: var(--gold);
  }

  .welcome-band {
    position: absolute; left: 0; top: 334px; width: 830px; height: 54px;
    background: var(--gold);
    transform: rotate(-4.2deg); transform-origin: left top;
    display: flex; align-items: center; padding-left: 66px;
  }
  .welcome-band p { color: var(--white); font-size: 28px; font-weight: 500; white-space: nowrap; }

  .intro {
    position: absolute; left: 24px; top: 448px; width: 470px;
    font-size: 18px; line-height: 1.3; color: var(--gold); text-align: center;
  }

  .try-badge {
    position: absolute; left: 540px; top: 330px; width: 250px; height: 250px; border-radius: 50%;
    background: var(--gold);
    display: flex; flex-direction: column; justify-content: center; align-items: center;
    color: var(--white); font-weight: 700; font-size: 50px; line-height: 1.02; text-align: center;
  }

  .product {
    position: absolute; left: 40px; width: 172px; height: 172px; border-radius: 50%;
    display: flex; align-items: center; justify-content: center; text-align: center;
    color: var(--berry); font-size: 25px; font-weight: 500; line-height: 1.15;
  }
  .product--cakes  { top: 505px; background: radial-gradient(circle at 40% 38%, var(--lemon-light) 0%, var(--lemon) 100%); }
  .product--creams { top: 718px; background: radial-gradient(circle at 40% 38%, var(--lilac-light) 0%, var(--lilac) 100%); }
  .product--cookie { top: 890px; background: radial-gradient(circle at 40% 38%, var(--mint-light) 0%, var(--mint) 100%); }

  .photo { position: absolute; border-radius: 10px; }
  .photo--bars {
    left: 300px; top: 516px; width: 236px; height: 136px;
    background: linear-gradient(160deg, #5a3b28 0%, #8a6446 45%, #d9b68a 100%);
  }
  .photo--tray {
    left: 282px; top: 668px; width: 344px; height: 210px;
    background: linear-gradient(160deg, #7a5236 0%, #b99a6c 50%, #e6e2da 100%);
  }

  .bubbles { position: absolute; border-radius: 50%; }
  .bubbles--top {
    right: -60px; top: -40px; width: 190px; height: 320px;
    background: radial-gradient(ellipse at center, rgba(200,155,211,.75) 0%, rgba(159,211,127,.55) 45%, rgba(244,211,60,0) 75%);
  }
  .bubbles--mid {
    right: -70px; top: 820px; width: 320px; height: 300px;
    background: radial-gradient(circle at 55% 50%, rgba(244,211,60,.7) 0%, rgba(200,155,211,.6) 40%, rgba(159,211,127,.4) 60%, rgba(255,255,255,0) 75%);
  }
  .bubbles--bottom {
    left: -60px; top: 1080px; width: 260px; height: 170px;
    background: radial-gradient(ellipse at center, rgba(159,211,127,.75) 0%, rgba(244,211,60,.55) 45%, rgba(255,255,255,0) 75%);
  }
  .bubbles--corner {
    right: -30px; top: 1060px; width: 330px; height: 180px;
    background: radial-gradient(ellipse at center, rgba(200,155,211,.8) 0%, rgba(244,211,60,.55) 45%, rgba(255,255,255,0) 75%);
  }
</style>
</head>
<body>
<main class="flyer">
  <svg class="backdrop" width="798" height="1200" viewBox="0 0 798 1200" aria-hidden="true">
    <path d="M0 0 H560 C520 120 420 230 0 330 Z" fill="#ffffff"/>
    <path d="M560 0 C560 110 680 190 798 215 V0 Z" fill="#b18a2c"/>
    <path d="M0 1085 C260 1110 560 1060 798 915 V1200 H0 Z" fill="#ffffff"/>
    <path d="M0 1085 C260 1110 560 1060 798 915 V940 C560 1085 260 1135 0 1110 Z" fill="#b18a2c"/>
  </svg>

  <div class="bubbles bubbles--top" role="img" aria-label="Cluster of pastel balloons"></div>

  <header>
    <div class="logo-art" role="img" aria-label="Brand illustration of stacked desserts"></div>
    <h1 class="brand-name">brinella</h1>
  </header>

  <div class="welcome-band"><p>Welcome to our new line of ice-cream desserts</p></div>

  <p class="intro">As everything else, all hand-made in our kitchen<br>only with natural ingredients.</p>

  <div class="try-badge"><span>TRY</span><span>OUR</span><span>NEW....</span></div>

  <div class="photo photo--bars" role="img" aria-label="Row of chocolate-dipped ice-cream cake bars on sticks"></div>
  <div class="photo photo--tray" role="img" aria-label="Tray of ice-cream pops rolled in nuts and sprinkles"></div>

  <section class="products">
    <div class="product product--cakes">Ice-cream<br>cakes</div>
    <div class="product product--creams">Ice-creams</div>
    <div class="product product--cookie">Cookie<br>ice-creams</div>
  </section>

  <div class="bubbles bubbles--mid" role="img" aria-label="Cluster of pastel balloons"></div>
  <div class="bubbles bubbles--bottom" role="img" aria-label="Cluster of pastel balloons"></div>
  <div class="bubbles bubbles--corner" role="img" aria-label="Cluster of pastel balloons"></div>
</main>
</body>
</html>
```